Wedding and event Photography company.

We need a business card design for a photography company based in Singapore named TamKeza. Our core service offering is wedding photojournalism. We would like to see minimalistic designs that use the colour white. The final design should communicate a sense of ease and reliability.

The attached are a couple of visual reference which i found over the web, i hope it will helps.

Project Brief Update (14th July 2014):
- Please refrain from using any images from the website for the design. The laws and regulations over here does not allow me to distribute my client's images. Thanks!

Target Market(s)

Young and middle aged adults aged 24 - 38. With money to spend =D

Industry/Entity Type

Business

Contact Information for Business Card

Name: Dev Lunor
Designation: Head Photographer
Mobile: +65 81749026
Email: jun@tamkeza.example
Website: www.tamkeza.example

Font styles to use
Other font styles liked:
• Baskerville URW

Colors

Designer to choose colors to be used in the design.

Requirements
Must have
• Must include:
• - The brand TamKeza
• - The logo attached
• - Please help to place the brand TamKeza with the logo according to your preferences.
• - Services
• - Wedding Photography
• - Portraiture
• - Photojournalism
Nice to have
• Looking forward to an elegant and simple design. Please see attached examples!
• Please use Serif Fonts
Should not have
• Please refrain from using dark tones for the majority of the design.
• Please refrain from letterpress and embossing.

```html
<!DOCTYPE html>
<html lang="en">
<head>
<meta charset="utf-8">
<title>TamKeza — Business Card</title>
<link href="https://fonts.googleapis.com/css2?family=Libre+Baskerville:wght@400&family=Jost:wght@400&display=swap" rel="stylesheet">
<style>
  :root {
    --backdrop: #d7a566;
    --card: #f3f3f6;
    --ink: #141414;
    --ink-soft: #2a2a2a;
    --shadow: rgba(70, 40, 10, 0.35);
  }
  * { margin: 0; padding: 0; box-sizing: border-box; }
  html, body {
    width: 1200px;
    height: 800px;
    overflow: hidden;
    background: var(--backdrop);
  }
  .stage {
    width: 1200px;
    height: 800px;
    display: flex;
    justify-content: center;
    align-items: center;
    gap: 64px;
  }
  .card {
    position: relative;
    width: 390px;
    height: 640px;
    background: var(--card);
    box-shadow: 4px 6px 14px var(--shadow);
    color: var(--ink);
    text-align: center;
  }
  .brand {
    position: absolute;
    left: 0;
    right: 0;
    font-family: "Libre Baskerville", serif;
    font-size: 44px;
    font-weight: 400;
    color: var(--ink);
    letter-spacing: 0.02em;
  }
  .card--front .brand { top: 218px; }
  .card--back .brand { top: 122px; }

  .services {
    position: absolute;
    top: 372px;
    left: 0;
    right: 0;
    list-style: none;
    font-family: "Jost", sans-serif;
    font-size: 17px;
    letter-spacing: 0.22em;
    line-height: 30px;
    color: var(--ink-soft);
  }
  .website {
    position: absolute;
    bottom: 52px;
    left: 0;
    right: 0;
    font-family: "Jost", sans-serif;
    font-size: 16px;
    letter-spacing: 0.24em;
    color: var(--ink-soft);
  }

  .person {
    position: absolute;
    top: 284px;
    left: 0;
    right: 0;
  }
  .person__name {
    font-family: "Libre Baskerville", serif;
    font-size: 29px;
    font-weight: 400;
    letter-spacing: 0.02em;
  }
  .person__title {
    margin-top: 6px;
    font-family: "Libre Baskerville", serif;
    font-size: 16px;
    letter-spacing: 0.16em;
  }
  .divider {
    position: absolute;
    top: 390px;
    left: 50%;
    width: 30px;
    height: 3px;
    margin-left: -15px;
    background: var(--ink);
  }
  .contact {
    position: absolute;
    top: 424px;
    left: 0;
    right: 0;
    list-style: none;
    font-family: "Jost", sans-serif;
    font-size: 16px;
    letter-spacing: 0.2em;
    line-height: 32px;
    color: var(--ink-soft);
  }
</style>
</head>
<body>
  <main class="stage">
    <section class="card card--front" aria-label="Card front">
      <div class="brand">TamKeza</div>
      <ul class="services">
        <li>Wedding</li>
        <li>Portraiture</li>
        <li>Events</li>
      </ul>
      <p class="website">www.tamkeza.example</p>
    </section>

    <section class="card card--back" aria-label="Card back">
      <div class="brand">TamKeza</div>
      <div class="person">
        <h1 class="person__name">Dev Lunor</h1>
        <p class="person__title">Head Photographer</p>
      </div>
      <div class="divider"></div>
      <ul class="contact">
        <li>jun@tamkeza.example</li>
        <li>+65 81749026</li>
        <li>www.tamkeza.example</li>
      </ul>
    </section>
  </main>
</body>
</html>
```